Jewelry Wholesale Business Card Design

Company name: VORELIA
Business Background: Wholesale jewelry store located in downtown Los Angeles. We specialize in 18k gold-filled, stainless steel, 14kt gold, and natural stone jewelry.
website: www.vorelia-sample.com
Instagram: vorelia_
Email: sales@vorelia-sample.com
Address: 318 W. MAPLE ST #27, #109
LOS ANGELES, CA 90014
(213)555-0172

We would like to create a simple, yet elegant business card for my store
-Includes company logo
-Black background preferred
-Gold metallic color letters
- Lists the type of products we sell
-Small icons for instagram handle, phone, email, and website

Target Market(s)

Hispanic community, age 12-40

Industry/Entity Type

Jewelry Wholesale

Contact Information for Business Card

logo, business location, website, phone number, email, instagram, lists type of products, Derek Malo(my name)

Font styles to use
Serif
Sans Serif

Colors
FFF300
FFF600
FEFA6F
FFFEC7
FFFEE8

Requirements
Must have
• logo, business location, website, phone number, email, instagram, lists type of products, Derek Malo(my name)

```html
<!DOCTYPE html>
<html lang="en">
<head>
<meta charset="utf-8">
<title>VORELIA Business Card</title>
<link href="https://fonts.googleapis.com/css2?family=Cinzel:wght@500&family=Roboto:wght@400;500&display=swap" rel="stylesheet">
<style>
  :root {
    --page-bg: #e6e7ea;
    --card-dark: #141414;
    --card-dark-soft: #2a2622;
    --panel-brown: #6e4f31;
    --panel-brown-deep: #5a3f27;
    --gold-bright: #fff300;
    --gold-strong: #fff600;
    --gold-soft: #fefa6f;
    --gold-pale: #fffec7;
    --gold-cream: #fffee8;
    --wordmark-ink: #141008;
  }
  * { margin: 0; padding: 0; box-sizing: border-box; }
  html, body { width: 1200px; height: 1200px; overflow: hidden; background: var(--page-bg); }
  .card {
    position: absolute; left: 229px; top: 357px; width: 742px; height: 486px;
    border-radius: 12px; overflow: hidden; background: var(--card-dark);
    font-family: "Roboto", Arial, sans-serif;
  }
  .card__photo {
    position: absolute; inset: 0;
    background: linear-gradient(160deg, var(--card-dark-soft) 0%, var(--card-dark) 55%, #1e1b18 100%);
  }
  .card__panel { position: absolute; inset: 0; }
  .card__mark {
    position: absolute; left: 38px; top: 205px;
    font-size: 36px; line-height: 44px; font-weight: 500; letter-spacing: 2px; color: var(--gold-bright);
  }
  .card__tagline {
    position: absolute; left: 38px; top: 345px; width: 312px;
    font-size: 21px; line-height: 28px; color: var(--gold-soft);
  }
  .card__wordmark {
    position: absolute; left: 389px; top: 82px;
    font-family: "Cinzel", "Times New Roman", serif; font-weight: 500;
    font-size: 52px; line-height: 60px; letter-spacing: 1px; color: var(--wordmark-ink);
  }
  .card__owner {
    position: absolute; left: 393px; top: 144px;
    font-size: 18px; line-height: 22px; font-weight: 500; letter-spacing: 2px; color: var(--gold-bright);
  }
  .contact { position: absolute; left: 393px; top: 180px; list-style: none; color: var(--gold-cream); font-size: 20px; line-height: 28px; }
  .contact__item { display: flex; align-items: flex-start; gap: 8px; }
  .contact__item + .contact__item { margin-top: 24px; }
  .contact__item--tight { margin-top: 0 !important; }
  .contact__icon { width: 16px; height: 16px; margin-top: 6px; flex: none; }
</style>
</head>
<body>
  <div class="card">
    <div class="card__photo" role="img" aria-label="Dark photograph of a model wearing gold rings and bracelets"></div>
    <svg class="card__panel" width="742" height="486" viewBox="0 0 742 486">
      <defs>
        <linearGradient id="panelFill" x1="0" y1="0" x2="1" y2="1">
          <stop offset="0" stop-color="var(--panel-brown)"/>
          <stop offset="1" stop-color="var(--panel-brown-deep)"/>
        </linearGradient>
        <linearGradient id="glowTop" x1="1" y1="0" x2="0" y2="1">
          <stop offset="0" stop-color="var(--gold-strong)" stop-opacity="1"/>
          <stop offset="1" stop-color="var(--gold-strong)" stop-opacity="0"/>
        </linearGradient>
        <linearGradient id="glowBottom" x1="1" y1="1" x2="0" y2="0">
          <stop offset="0" stop-color="var(--gold-strong)" stop-opacity="1"/>
          <stop offset="1" stop-color="var(--gold-strong)" stop-opacity="0"/>
        </linearGradient>
      </defs>
      <polygon points="447,0 742,0 742,486 403,486 215,239" fill="url(#panelFill)" role="img" aria-label="Warm brown panel over a faint photograph of jewelry"/>
      <line x1="447" y1="0" x2="215" y2="239" stroke="url(#glowTop)" stroke-width="3"/>
      <line x1="403" y1="486" x2="215" y2="239" stroke="url(#glowBottom)" stroke-width="3"/>
    </svg>

    <div class="card__mark">VORELIA</div>
    <p class="card__tagline">We specialize in 18k gold-filled, stainless steel, 14kt gold, and natural stone jewelry.</p>

    <div class="card__wordmark">VORELIA</div>
    <div class="card__owner">DEREK MALO</div>

    <ul class="contact">
      <li class="contact__item">
        <svg class="contact__icon" viewBox="0 0 16 16"><path d="M8 1a5 5 0 0 0-5 5c0 4 5 9 5 9s5-5 5-9a5 5 0 0 0-5-5zm0 7a2 2 0 1 1 0-4 2 2 0 0 1 0 4z" fill="var(--gold-bright)"/></svg>
        <span>318 W. MAPLE ST #27, #109<br>LOS ANGELES, CA 90014</span>
      </li>
      <li class="contact__item">
        <svg class="contact__icon" viewBox="0 0 16 16"><path d="M3.5 1.5l2.5 0.5 1 3-1.7 1.2a9 9 0 0 0 4.5 4.5L11 9l3 1 .5 2.5-2 2C7 14.5 1.5 9 1.5 3.5z" fill="var(--gold-bright)"/></svg>
        <span>(213)555-0172</span>
      </li>
      <li class="contact__item">
        <svg class="contact__icon" viewBox="0 0 16 16" fill="none" stroke="var(--gold-bright)" stroke-width="1.4"><circle cx="8" cy="8" r="6.5"/><ellipse cx="8" cy="8" rx="3" ry="6.5"/><line x1="1.5" y1="8" x2="14.5" y2="8"/></svg>
        <span>WWW.VORELIA-SAMPLE.COM</span>
      </li>
      <li class="contact__item contact__item--tight">
        <svg class="contact__icon" viewBox="0 0 16 16" fill="none" stroke="var(--gold-bright)" stroke-width="1.6"><circle cx="8" cy="8" r="3"/><path d="M11 8v1.3a2 2 0 0 0 4 0V8a7 7 0 1 0-3 5.7"/></svg>
        <span>SALES@VORELIA-SAMPLE.COM</span>
      </li>
      <li class="contact__item">
        <svg class="contact__icon" viewBox="0 0 16 16" fill="none" stroke="var(--gold-bright)" stroke-width="1.6"><rect x="2" y="2" width="12" height="12" rx="3"/></svg>
        <span>VORELIA_</span>
      </li>
    </ul>
  </div>
</body>
</html>
```